Poster for a variety show

This poster is for a one time variety show with a magician, juggler and ventriloquist. This is a family friendly show with a religious message along with the performances. The poster should be very colorful in a vertical 11"x14" size. The name of the show is "Wonderstruck" which should be prominently featured. This is a colorful show business type poster that should convey energy and excitment

Location: Halvern College of Mountain Studies at Pinecrest Ridge, Marrowfield Auditorium
Date: July 31, 2013 at 7:00 pm
Free Admission
Starring: Illusionist Tomas Brevik, World Record Juggler Oscar Pell and Ventriloquist Neil Fosberg

Words or phrases that might be used in the poster: Amazing Illusions, Spectacular Juggling, Family Friendly Comedy, Audience Participation, Spiritually Uplifting Message

Target Market(s)

Families, college students

Industry/Entity Type

Religious

Requirements
Must have
• Must have time, date and location and use the three photos of the performers. Name "Wonderstruck" should be prominently featured.
Should not have
• Do not use the word "magic" or "magical"

```html
<!DOCTYPE html>
<html lang="en">
<head>
<meta charset="utf-8">
<title>Wonderstruck Variety Show</title>
<link rel="stylesheet" href="https://fonts.googleapis.com/css2?family=Amatic+SC:wght@400;700&display=swap">
<style>
  :root {
    --red: #d42a2f;
    --blue: #2a63d4;
    --yellow: #fbe83a;
    --ink: #111111;
    --paper: #ffffff;
    --display: "Amatic SC", "Arial Narrow", sans-serif;
    --body: Arial, Helvetica, sans-serif;
  }
  * { box-sizing: border-box; margin: 0; padding: 0; }
  html, body { width: 943px; height: 1200px; overflow: hidden; background: var(--paper); }
  .poster { position: relative; width: 943px; height: 1200px; background: var(--paper); }

  .show-title {
    position: absolute; left: 0; top: 20px; width: 943px;
    text-align: center; font-family: var(--display); font-weight: 700;
    font-size: 196px; line-height: 1; letter-spacing: 2px; color: var(--red);
    white-space: nowrap;
  }
  .show-subtitle {
    position: absolute; left: 0; top: 190px; width: 943px;
    text-align: center; font-family: var(--display); font-weight: 700;
    font-size: 86px; line-height: 1; color: var(--blue); letter-spacing: 3px;
    white-space: nowrap;
  }

  .badge {
    position: absolute; border-radius: 50%;
    display: flex; align-items: center; justify-content: center; text-align: center;
    font-family: var(--display); font-weight: 700; line-height: 0.95; color: var(--ink);
  }
  .badge--participation { left: 45px; top: 205px; width: 182px; height: 182px; background: var(--red); font-size: 34px; }
  .badge--performers { left: 336px; top: 294px; width: 160px; height: 160px; background: var(--blue); font-size: 32px; }
  .badge--comedy { left: 717px; top: 721px; width: 146px; height: 146px; background: var(--yellow); font-size: 34px; }
  .badge--message { left: 747px; top: 991px; width: 174px; height: 174px; background: var(--red); font-size: 34px; }

  .performer {
    position: absolute; border-radius: 50%; overflow: hidden; border-style: solid;
  }
  .performer__photo { position: absolute; inset: 0; }
  .performer__caption {
    position: absolute; left: 0; right: 0; height: 32px;
    color: var(--ink); white-space: nowrap;
    font-family: var(--body); font-size: 18px; line-height: 32px; text-align: center;
  }

  .performer--illusionist { left: 20px; top: 416px; width: 400px; height: 400px; border-width: 26px; border-color: var(--yellow); }
  .performer--illusionist .performer__photo { background: radial-gradient(circle at 45% 35%, #33507e 0%, #13234a 55%, #070d22 100%); }
  .performer--illusionist .performer__caption { top: 250px; background: var(--yellow); }

  .performer--juggler { left: 511px; top: 291px; width: 400px; height: 400px; border-width: 26px; border-color: var(--red); }
  .performer--juggler .performer__photo { background: linear-gradient(180deg, #f4f4f4 0%, #ecdcd6 45%, #c8383a 75%, #a82225 100%); }
  .performer--juggler .performer__caption { top: 236px; background: var(--red); font-size: 17px; }

  .performer--ventriloquist { left: 369px; top: 736px; width: 334px; height: 334px; border-width: 22px; border-color: var(--blue); }
  .performer--ventriloquist .performer__photo { background: radial-gradient(circle at 50% 40%, #5a4a45 0%, #3a1d1c 50%, #1c0b0b 100%); }
  .performer--ventriloquist .performer__caption { top: 196px; background: var(--blue); font-size: 17px; }

  .details { position: absolute; left: 40px; top: 848px; width: 300px; text-align: center; }
  .details__heading {
    font-family: var(--display); font-weight: 700; font-size: 50px; line-height: 1; color: var(--red);
  }
  .details__text { font-family: var(--body); font-size: 20px; line-height: 25px; color: var(--ink); }
  .details__text--venue { margin-top: 4px; }
  .details__heading--date { margin-top: 16px; }
  .details__heading--admission { margin-top: 18px; }
</style>
</head>
<body>
<main class="poster">
  <h1 class="show-title">WONDERSTRUCK</h1>
  <p class="show-subtitle">VARIETY SHOW</p>

  <div class="badge badge--participation">AUDIENCE<br>PARTICIPATION</div>
  <div class="badge badge--performers">AMAZING<br>PERFORMERS</div>

  <figure class="performer performer--juggler">
    <div class="performer__photo" role="img" aria-label="Photo of juggler Oscar Pell holding juggling balls, clubs and rings"></div>
    <figcaption class="performer__caption">World Record Juggler Oscar Pell</figcaption>
  </figure>

  <figure class="performer performer--illusionist">
    <div class="performer__photo" role="img" aria-label="Photo of illusionist Tomas Brevik in a dark jacket against a blue backdrop"></div>
    <figcaption class="performer__caption">Illusionist Tomas Brevik</figcaption>
  </figure>

  <figure class="performer performer--ventriloquist">
    <div class="performer__photo" role="img" aria-label="Photo of ventriloquist Neil Fosberg with his rat puppet on stage"></div>
    <figcaption class="performer__caption">Ventriloquist Neil Fosberg</figcaption>
  </figure>

  <div class="badge badge--comedy">FAMILY<br>FRIENDLY<br>COMEDY</div>
  <div class="badge badge--message">SPIRITUALLY<br>UPLIFTING<br>MESSAGE</div>

  <section class="details">
    <h2 class="details__heading">LOCATION</h2>
    <p class="details__text details__text--venue">Halvern College of Mountain Studies at Pinecrest Ridge, Marrowfield Auditorium</p>
    <h2 class="details__heading details__heading--date">DATE</h2>
    <p class="details__text">July 31, 2013<br>7:00 pm</p>
    <h2 class="details__heading details__heading--admission">FREE ADMISSION</h2>
  </section>
</main>
</body>
</html>
```